Flyer-Design für Dachrinnenreinigung
Zielgruppe
Dienstleistung Hauptsächlich Eigenheimbesitzer, Hausverwalter, Behörden, Schulen
Aufgabenstellung
Farblich bitte etwas passend zum Logo und wie unsere Homepage:
www.Traufwerk-pflegen.de
Diesen Flyer bekommen Privatkunden der Dachrinnenreinigung nach einer Reinigung mit der Rechnung.
Seite 1:
Der Flyer soll animieren Durch einen Treuebonus 15 € Gutschrift für die nächste Reinigung bei Abgabe einer Fundor Bewertung.
Seite 2
Und er soll hinweisen auf unsere weiteren Dienstleistungen:
- Dachrinnensanierung
- Schornsteinverkleidung
- Dachfenster Austausch
- Gauben- Giebelverkleidung

```html
<!DOCTYPE html>
<html lang="de">
<head>
<meta charset="utf-8">
<title>Traufwerk-pflegen.de – Flyer</title>
<link rel="stylesheet" href="https://fonts.googleapis.com/css2?family=Bebas+Neue&family=Lilita+One&family=Quicksand:wght@600&display=swap">
<style>
  :root {
    --brand-blue: #25378f;
    --ink: #3f3d48;
    --paper: #ffffff;
    --stage: #d6d6d6;
    --strip: rgba(235, 235, 238, 0.82);
  }
  * { margin: 0; padding: 0; box-sizing: border-box; }
  html, body { width: 1200px; height: 846px; overflow: hidden; }
  body { background: var(--stage); position: relative; font-family: "Bebas Neue", sans-serif; }

  .flyer {
    position: absolute; top: 85px; width: 478px; height: 675px;
    background: var(--paper); overflow: hidden;
  }
  .flyer--front { left: 81px; }
  .flyer--back { left: 641px; }

  .masthead {
    height: 150px; display: flex; flex-direction: column;
    align-items: center; justify-content: center; gap: 10px;
  }
  .brand { display: flex; align-items: center; gap: 10px; }
  .brand__square { width: 22px; height: 22px; background: var(--brand-blue); }
  .brand__name {
    font-family: "Bebas Neue", sans-serif; font-size: 52px; line-height: 1;
    letter-spacing: 1px; color: var(--brand-blue);
  }
  .tagline {
    font-family: "Quicksand", sans-serif; font-weight: 600;
    font-size: 12px; letter-spacing: 1.2px; color: var(--ink);
  }

  .stage-area { position: absolute; top: 150px; left: 0; width: 478px; height: 466px; }
  .photo-bg--front {
    background: linear-gradient(110deg, #7f8a86 0%, #a9a796 28%, #d8c57a 48%, #e6cf6e 62%, #b9b3a0 80%, #8e949c 100%);
  }
  .photo-bg--back {
    background: linear-gradient(120deg, #8fb0d4 0%, #a7a9b0 30%, #9a8a80 48%, #b5b4b6 66%, #7d7d80 100%);
  }

  .strip {
    position: absolute; background: var(--strip); color: var(--ink);
    line-height: 1; white-space: nowrap; padding: 3px 6px 0;
    transform-origin: left center;
  }
  .strip--blue { color: var(--brand-blue); }
  .strip .accent { color: var(--brand-blue); }

  .offer__intro { left: 0; top: 228px; font-size: 30px; transform: rotate(-3.5deg); }
  .offer__amount {
    position: absolute; left: 95px; top: 258px;
    font-family: "Lilita One", sans-serif; font-size: 150px; line-height: 1;
    color: var(--brand-blue); letter-spacing: -4px;
    transform: rotate(-3deg);
    text-shadow: 3px 0 #fff, -3px 0 #fff, 0 3px #fff, 0 -3px #fff,
                 2px 2px #fff, -2px -2px #fff, 2px -2px #fff, -2px 2px #fff,
                 4px 5px 6px rgba(0,0,0,0.35);
  }
  .offer__cont { left: 0; top: 407px; font-size: 30px; transform: rotate(-3.5deg); padding-left: 10px; }
  .offer__review { left: 0; top: 450px; font-size: 36px; transform: rotate(-3.5deg); padding-left: 12px; }
  .offer__review .small { color: var(--ink); font-size: 28px; }
  .listing-badge {
    position: absolute; left: 256px; top: 480px; width: 192px; height: 72px;
    background: #fff; border: 2px solid var(--brand-blue);
    transform: rotate(-12deg); box-shadow: 2px 3px 6px rgba(0,0,0,0.35);
  }

  .services__title {
    position: absolute; top: 190px; left: 0; width: 478px; text-align: center;
    font-size: 32px; color: var(--ink); line-height: 1;
  }
  .services__title .accent { color: var(--brand-blue); font-size: 38px; }
  .service { font-size: 27px; color: var(--brand-blue); padding: 2px 6px 0; }
  .service--alt { color: var(--ink); }
  .service--1 { left: 12px; top: 286px; }
  .service--2 { left: 178px; top: 380px; }
  .service--3 { left: 16px; top: 479px; }
  .service--4 { left: 165px; top: 540px; }

  .snapshot {
    position: absolute; border: 3px solid var(--brand-blue);
    box-shadow: 2px 3px 6px rgba(0,0,0,0.4);
  }
  .snapshot--gutter {
    left: 276px; top: 245px; width: 152px; height: 112px; transform: rotate(9deg);
    background: linear-gradient(150deg, #8aa48c 0%, #6f7378 40%, #9aa3ad 65%, #5a4a45 100%);
  }
  .snapshot--chimney {
    left: 46px; top: 322px; width: 104px; height: 136px; transform: rotate(-4deg);
    background: linear-gradient(180deg, #3d7fd0 0%, #4f8fd8 40%, #4b4d55 62%, #6b5a52 100%);
    border-color: #5a5a60;
  }

  .footer {
    position: absolute; bottom: 0; left: 0; width: 478px; height: 59px;
    text-align: center; background: var(--paper);
  }
  .footer__url { font-size: 29px; color: var(--brand-blue); line-height: 1; padding-top: 6px; }
  .footer__contact { font-size: 16px; color: var(--ink); margin-top: 3px; word-spacing: 1px; }
  .footer__contact .label { color: var(--brand-blue); }
  .footer__contact .gap { display: inline-block; width: 16px; }
</style>
</head>
<body>

<section class="flyer flyer--front">
  <header class="masthead">
    <div class="brand"><span class="brand__square"></span><span class="brand__name">TRAUFWERK-PFLEGEN.DE</span></div>
    <p class="tagline">schnell, zuverlässig, flexibel</p>
  </header>
  <div class="stage-area photo-bg--front" role="img" aria-label="Unscharfes Foto einer Dachrinne vor gelber Dachbahn und Holzlatten"></div>

  <p class="strip offer__intro">SIE&nbsp; WOLLEN BEI DER NÄCHSTEN REINIGUNG</p>
  <p class="offer__amount">15€</p>
  <p class="strip offer__cont">SPAREN, DANN LASSEN SIE DOCH EINE</p>
  <p class="strip offer__review"><span class="accent">FUNDOR BEWERTUNG</span> <span class="small">DA !</span></p>
  <div class="listing-badge" aria-hidden="true"></div>

  <footer class="footer">
    <p class="footer__url">WWW.TRAUFWERK-PFLEGEN.DE</p>
    <p class="footer__contact"><span class="label">ADRESSE:</span> LINDENHANG 8, 21345 HOLLBECK<span class="gap"></span><span class="label">TELEFON:</span> 04178-552 1093</p>
  </footer>
</section>

<section class="flyer flyer--back">
  <header class="masthead">
    <div class="brand"><span class="brand__square"></span><span class="brand__name">TRAUFWERK-PFLEGEN.DE</span></div>
    <p class="tagline">schnell, zuverlässig, flexibel</p>
  </header>
  <div class="stage-area photo-bg--back" role="img" aria-label="Unscharfes Foto einer Kupferdachrinne vor blauem Himmel"></div>

  <h2 class="services__title">WEITERE <span class="accent">DIENSTLEISTUNGEN</span> VON UNS</h2>
  <div class="snapshot snapshot--gutter" role="img" aria-label="Foto: Handwerker beim Löten einer Dachrinne"></div>
  <div class="snapshot snapshot--chimney" role="img" aria-label="Foto: mit Schiefer verkleideter Schornstein auf Ziegeldach"></div>
  <p class="strip service service--1">- DACHRINNENSANIERUNG</p>
  <p class="strip service service--alt service--2">- SCHORNSTEINVERKLEIDUNG</p>
  <p class="strip service service--3">- DACHFENSTER AUSTAUSCH</p>
  <p class="strip service service--alt service--4">- GAUBEN- GIEBELVERKLEIDUNG</p>

  <footer class="footer">
    <p class="footer__url">WWW.TRAUFWERK-PFLEGEN.DE</p>
    <p class="footer__contact"><span class="label">ADRESSE:</span> LINDENHANG 8, 21345 HOLLBECK<span class="gap"></span><span class="label">TELEFON:</span> 04178-552 1093</p>
  </footer>
</section>

</body>
</html>
```